Luxury Caviar Tin Label for High End Caviar Retailer

We are looking for a new caviar label design. We want something unique, preferably black and gold or dark blue and gold. We want a modern and luxurious feel. We have several types of caviar so we need to be able to change the name of the caviar when we print the labels. See inspiration attached. Logo is also attached. More about us: velmoronfare.com

Industry/Entity Type

fine foods industry, caviar

Font styles to use
Serif
Decorative

Requirements
Must have
• KT Velmoron Logo, space for caviar name
Nice to have
• black and gold, blue and gold

```html
<!DOCTYPE html>
<html lang="en">
<head>
<meta charset="utf-8">
<title>KT Velmoron – Hackleback Caviar Tin Labels</title>
<link rel="stylesheet" href="https://fonts.googleapis.com/css2?family=Cinzel:wght@500&family=Marcellus&family=Cormorant+Garamond:wght@600&display=swap">
<style>
  :root {
    --paper: #ffffff;
    --tin-black: #050505;
    --label-black: #0b0b0b;
    --gold: #c9a04a;
    --gold-light: #f1d58a;
    --gold-deep: #8a6424;
  }
  html, body {
    margin: 0;
    padding: 0;
    width: 1200px;
    height: 1200px;
    overflow: hidden;
    background: var(--paper);
  }
  .label-sheet { display: block; width: 1200px; height: 1200px; }
  .tin-face { fill: var(--tin-black); }
  .inner-field { fill: var(--label-black); }
  .gold-rule { fill: none; stroke: url(#goldSheen); }
  .variety-arc {
    font-family: "Cinzel", serif;
    font-weight: 500;
    font-size: 19px;
    letter-spacing: 2.4px;
    fill: url(#goldSheen);
  }
  .brand-name {
    font-family: "Marcellus", serif;
    font-size: 12.5px;
    letter-spacing: 0.4px;
    fill: var(--gold);
  }
  .brand-mark { fill: none; stroke: var(--gold); stroke-width: 1.4; }
  .selection-line {
    font-family: "Marcellus", serif;
    font-size: 8px;
    letter-spacing: 0.5px;
    fill: var(--gold);
  }
  .product-name {
    font-family: "Marcellus", serif;
    font-size: 31px;
    letter-spacing: 1.5px;
    fill: url(#goldSheen);
  }
  .care-info {
    font-family: "Cormorant Garamond", serif;
    font-weight: 600;
    font-size: 7.6px;
    fill: var(--gold);
  }
  .border-band { fill: none; stroke: url(#goldSheen); stroke-width: 9; opacity: 0.85; }
</style>
</head>
<body>
<svg class="label-sheet" viewBox="0 0 1200 1200" xmlns="http://www.w3.org/2000/svg" xmlns:xlink="http://www.w3.org/1999/xlink">
  <defs>
    <linearGradient id="goldSheen" x1="0" y1="0" x2="1" y2="1">
      <stop offset="0" stop-color="#8a6424"/>
      <stop offset="0.3" stop-color="#f1d58a"/>
      <stop offset="0.55" stop-color="#b88a36"/>
      <stop offset="0.8" stop-color="#e9c978"/>
      <stop offset="1" stop-color="#7d5a1f"/>
    </linearGradient>
    <path id="topArc" d="M -112 0 A 112 112 0 0 1 112 0" transform="rotate(0)"/>
    <path id="bottomArc" d="M -107.4 62 A 124 124 0 0 0 107.4 62"/>

    <symbol id="caviarLabel" viewBox="-164 -164 328 328" overflow="visible">
      <circle class="tin-face" r="164"/>
      <circle class="inner-field" r="105"/>
      <circle class="gold-rule" r="105" stroke-width="0.9"/>
      <path class="gold-rule" stroke-width="1.2" d="M -118.9 -30.6 A 123 123 0 0 0 -118.9 30.6"/>
      <path class="gold-rule" stroke-width="1.2" d="M 118.9 -30.6 A 123 123 0 0 1 118.9 30.6"/>
      <text class="variety-arc" text-anchor="middle"><textPath href="#topArc" startOffset="50%">HACKLEBACK CAVIAR</textPath></text>
      <circle class="brand-mark" cx="0" cy="-50" r="18"/>
      <text class="brand-name" x="0" y="-15" text-anchor="middle">KT VELMORON</text>
      <line class="gold-rule" x1="-31" y1="9" x2="31" y2="9" stroke-width="1"/>
      <text class="selection-line" x="0" y="30" text-anchor="middle">EXCLUSIVE SELECTION</text>
      <text class="product-name" x="0" y="66" text-anchor="middle">CAVIAR</text>
      <text class="care-info" text-anchor="middle"><textPath href="#bottomArc" startOffset="50%">Keep Refrigerated 28 - 34 | www.velmoronfare.com | Ingredients: caviar - salt</textPath></text>
    </symbol>
  </defs>

  <g class="label label--beaded" transform="translate(220 225)">
    <use href="#caviarLabel" x="-164" y="-164" width="328" height="328"/>
    <circle class="border-band" r="155" role="img" aria-label="Gold beaded border band between fine rings"/>
  </g>
  <g class="label label--key" transform="translate(603 225)">
    <use href="#caviarLabel" x="-164" y="-164" width="328" height="328"/>
    <circle class="border-band" r="154" stroke-width="12" role="img" aria-label="Gold band with repeating geometric key motif"/>
  </g>
  <g class="label label--waves" transform="translate(989 225)">
    <use href="#caviarLabel" x="-164" y="-164" width="328" height="328"/>
    <circle class="border-band" r="153" stroke-width="14" role="img" aria-label="Gold band of interlocking wave scrolls"/>
  </g>

  <g class="label label--double-rule" transform="translate(220 603)">
    <use href="#caviarLabel" x="-164" y="-164" width="328" height="328"/>
    <circle class="border-band" r="156" stroke-width="6" role="img" aria-label="Gold double rule with dotted edges"/>
  </g>
  <g class="label label--rings" transform="translate(603 603)">
    <use href="#caviarLabel" x="-164" y="-164" width="328" height="328"/>
    <circle class="border-band" r="156" stroke-width="7" opacity="0.6" role="img" aria-label="Chain of small gold rings around the edge"/>
  </g>
  <g class="label label--rope" transform="translate(989 603)">
    <use href="#caviarLabel" x="-164" y="-164" width="328" height="328"/>
    <circle class="border-band" r="158" stroke-width="5" role="img" aria-label="Fine gold twisted rope edge"/>
  </g>

  <g class="label label--filigree" transform="translate(603 981)">
    <use href="#caviarLabel" x="-164" y="-164" width="328" height="328"/>
    <circle class="border-band" r="151" stroke-width="12" opacity="0.5" role="img" aria-label="Gold filigree scrollwork border"/>
  </g>
</svg>
</body>
</html>
```